Business Card Design Project

We would need a business name card for our online website business, http://www.brindle.com.sg/. We would need to include our website on the name card as well.

Target Market(s)

Adults and kids in Singapore, mainly expatriates

Industry/Entity Type

Business

Font styles to use
Sans Serif

Colors

Designer to choose colors to be used in the design.

Requirements
Must have
• Must include our "vorn" logo and we would like our name card to be printed on light craft paper material

```html
<!DOCTYPE html>
<html lang="en">
<head>
<meta charset="utf-8">
<title>Vorn business card</title>
<link rel="stylesheet" href="https://fonts.googleapis.com/css2?family=Open+Sans:wght@400;600;700;800&display=swap">
<style>
  :root {
    --navy: #233a78;
    --red: #d0202f;
    --ink: #1a1a1a;
    --paper: #ffffff;
    --backdrop: #e7e1d6;
  }
  * { margin: 0; padding: 0; box-sizing: border-box; }
  html, body {
    width: 1200px; height: 1023px; overflow: hidden;
    background: var(--backdrop);
    font-family: "Open Sans", Arial, sans-serif;
  }
  .canvas { position: relative; width: 1200px; height: 1023px; }
  .card {
    position: absolute;
    width: 560px; height: 320px;
    background: var(--paper);
    box-shadow: 0 4px 14px rgba(0,0,0,.18);
    overflow: hidden;
  }
  .card--front { left: 70px; top: 110px; }
  .card--back { left: 570px; top: 560px; }

  .wordmark {
    font-weight: 800; color: var(--navy);
    letter-spacing: 2px; text-transform: uppercase; line-height: 1;
  }

  .card--front .wordmark {
    position: absolute; left: 0; right: 0; top: 100px;
    text-align: center; font-size: 64px;
  }
  .front__url {
    position: absolute; left: 0; right: 0; top: 212px;
    text-align: center; font-weight: 700; font-size: 22px; color: var(--ink); letter-spacing: .5px;
  }

  .card--back .wordmark {
    position: absolute; left: 40px; top: 64px; font-size: 44px;
  }

  .person { position: absolute; left: 300px; top: 92px; }
  .person__name { font-weight: 800; font-size: 20px; color: var(--navy); letter-spacing: .5px; text-transform: uppercase; line-height: 1.2; }
  .person__role { font-size: 15px; color: var(--red); line-height: 1.3; }

  .contacts { position: absolute; left: 272px; top: 160px; list-style: none; }
  .contacts__item { display: flex; align-items: center; gap: 10px; font-size: 16px; color: var(--navy); height: 27px; white-space: nowrap; }
  .contacts__icon { width: 15px; height: 15px; flex: none; }

  .band { position: absolute; left: 0; }
  .band--navy-step { bottom: 0; width: 70px; height: 56px; background: var(--navy); }
  .band--red { left: 70px; right: 0; bottom: 16px; height: 7px; background: var(--red); }
  .band--navy { left: 70px; right: 0; bottom: 0; height: 16px; background: var(--navy); }
</style>
</head>
<body>
<main class="canvas">

  <section class="card card--front" aria-label="Card front">
    <p class="wordmark">vorn</p>
    <p class="front__url">www.brindle.com.sg</p>
  </section>

  <section class="card card--back" aria-label="Card back">
    <p class="wordmark">vorn</p>

    <div class="person">
      <p class="person__name">Martin Hale</p>
      <p class="person__role">Director</p>
    </div>

    <ul class="contacts">
      <li class="contacts__item">
        <svg class="contacts__icon" viewBox="0 0 16 16"><path fill="#d0202f" d="M3.5 1.5l2.5 3-1.5 1.6c.8 1.8 2.1 3.1 3.9 3.9L10 8.5l3 2.5-1.3 2.4C7 13.5 2.5 9 2.6 3.2z"/></svg>
        (+65) 6310 4482
      </li>
      <li class="contacts__item">
        <svg class="contacts__icon" viewBox="0 0 16 16"><rect x="4" y="1.5" width="8" height="4" fill="#d0202f"/><rect x="1.5" y="5.5" width="13" height="6" rx="1" fill="#d0202f"/><rect x="4" y="9.5" width="8" height="5" fill="#fff" stroke="#d0202f" stroke-width="1.4"/></svg>
        (+65) 6310 4489
      </li>
      <li class="contacts__item">
        <svg class="contacts__icon" viewBox="0 0 16 16"><rect x="1" y="3.5" width="14" height="9.5" fill="#d0202f"/><path d="M1.5 4l6.5 5 6.5-5" fill="none" stroke="#fff" stroke-width="1.3"/></svg>
        email@vorncorp.com
      </li>
      <li class="contacts__item">
        <svg class="contacts__icon" viewBox="0 0 16 16"><circle cx="8" cy="8" r="7" fill="#d0202f"/><path d="M1 8h14M8 1c-3 3.5-3 10.5 0 14M8 1c3 3.5 3 10.5 0 14" fill="none" stroke="#fff" stroke-width="1"/></svg>
        www.brindle.com.sg
      </li>
    </ul>

    <div class="band band--navy-step"></div>
    <div class="band band--red"></div>
    <div class="band band--navy"></div>
  </section>

</main>
</body>
</html>
```